Modern business card for triathlon training business in Australia

We need a business card design for our triathlon training company.

Lakeshore Pace Fitness is an Australian business, owned by women, run for women. Lakeshore Pace Fitness helps women prepare or improve triathlon skills and confidence through triathlon camps completely designed for women.

Our camps focus on preparing women both physically and mentally for their next (or first!) triathlon.

You can see our website www.lakeshorepacefitness.com.au for more info about our business and our style.

We've attached two of our logos and are happy to consider a design that utilised either colour scheme with the teal colour being our 'feature' colour. We don't want overly feminine cards but rather cards that are professional and neat. If the inclusion of any pictures/art is warranted, this should be focused on our swim/ride/run theme and in that specific order (swim/ride/run).

The business card needs to be a printable design and the contact details will need to change for our two employees.

Target Market(s)

Female clients and partners/vendors/sponsors that we work with in the triathlon industry

Industry/Entity Type

Fitness

Contact Information for Business Card

Lakeshore Pace Fitness (business name)
Maren Dunley
Business Director
Mobile: 0455 918 237
Email: maren@lakeshorepacefitness.com.au
www.lakeshorepacefitness.com.au

Second business card:
Lakeshore Pace Fitness
Bea Calvert
Coaching Director
Mobile: 0433 206 519
Email: bea@lakeshorepacefitness.com.au

Font styles to use
Serif
Sans Serif

Requirements
Must have
• Core contact details above, our logo and be a printable design
Should not have
• Pink
• Cursive/script fonts

```html
<!DOCTYPE html>
<html lang="en">
<head>
<meta charset="utf-8">
<title>Lakeshore Pace Fitness — Business Card</title>
<link href="https://fonts.googleapis.com/css2?family=Open+Sans:wght@400;600;700;800&display=swap" rel="stylesheet">
<style>
  :root {
    --teal: #1fc3cf;
    --teal-light: #36d4dd;
    --teal-deep: #14a9b6;
    --white: #ffffff;
    --tab: #eef3f4;
    --page: #e7ecee;
  }
  * { margin: 0; padding: 0; box-sizing: border-box; }
  html, body { width: 1200px; height: 1022px; overflow: hidden; }
  body {
    background: var(--page);
    font-family: "Open Sans", Arial, sans-serif;
    position: relative;
  }
  .card {
    position: absolute;
    left: 198px;
    width: 804px;
    height: 459px;
    overflow: hidden;
    background: linear-gradient(160deg, var(--teal-light) 0%, var(--teal) 45%, var(--teal-deep) 100%);
    color: var(--white);
    box-shadow: 0 6px 18px rgba(0, 60, 70, 0.18);
  }
  .card--front { top: 38px; }
  .card--back { top: 525px; }

  .corner-tab {
    position: absolute;
    width: 230px;
    height: 52px;
    background: var(--tab);
    border-radius: 26px;
  }
  .corner-tab--top-right { top: -26px; right: -26px; }
  .corner-tab--bottom-left { bottom: -26px; left: -26px; }

  /* Front: brand name */
  .brand {
    position: absolute;
    right: 70px;
    top: 190px;
    display: flex;
    align-items: center;
    gap: 18px;
  }
  .brand-dot {
    width: 46px;
    height: 46px;
    border-radius: 50%;
    background: var(--white);
  }
  .brand-name {
    font-weight: 800;
    font-size: 38px;
    letter-spacing: 1px;
    text-transform: uppercase;
    color: var(--white);
    line-height: 1;
  }

  /* Back: contact details */
  .contact {
    position: absolute;
    left: 60px;
    top: 150px;
  }
  .person-name {
    font-weight: 700;
    font-size: 40px;
    line-height: 1.1;
  }
  .person-role {
    font-weight: 700;
    font-size: 20px;
    margin-bottom: 34px;
  }
  .contact-list { list-style: none; }
  .contact-item {
    display: flex;
    align-items: center;
    gap: 18px;
    font-size: 22px;
    font-weight: 400;
    margin-bottom: 14px;
  }
  .contact-icon { width: 24px; height: 24px; flex: none; }
</style>
</head>
<body>

  <section class="card card--front" aria-label="Card front">
    <span class="corner-tab corner-tab--top-right"></span>
    <span class="corner-tab corner-tab--bottom-left"></span>
    <div class="brand">
      <span class="brand-dot"></span>
      <span class="brand-name">Lakeshore Pace Fitness</span>
    </div>
  </section>

  <section class="card card--back" aria-label="Card back">
    <span class="corner-tab corner-tab--top-right"></span>
    <span class="corner-tab corner-tab--bottom-left"></span>
    <div class="contact">
      <h1 class="person-name">Maren Dunley</h1>
      <p class="person-role">Business Director</p>
      <ul class="contact-list">
        <li class="contact-item">
          <svg class="contact-icon" viewBox="0 0 24 24" fill="none" stroke="#fff" stroke-width="2"><rect x="6" y="2" width="12" height="20" rx="2"/><line x1="10" y1="18" x2="14" y2="18"/></svg>
          <span>0455 918 237</span>
        </li>
        <li class="contact-item">
          <svg class="contact-icon" viewBox="0 0 24 24" fill="none" stroke="#fff" stroke-width="2"><circle cx="12" cy="12" r="10"/><ellipse cx="12" cy="12" rx="4" ry="10"/><line x1="2" y1="12" x2="22" y2="12"/></svg>
          <span>www.lakeshorepacefitness.com.au</span>
        </li>
        <li class="contact-item">
          <svg class="contact-icon" viewBox="0 0 24 24" fill="none" stroke="#fff" stroke-width="2"><rect x="2" y="5" width="20" height="14" rx="1"/><polyline points="2,5 12,13 22,5"/></svg>
          <span>maren@lakeshorepacefitness.com.au</span>
        </li>
      </ul>
    </div>
  </section>

</body>
</html>
```